Game, Voice & Dedicated Server Company Needs a Business Card Design

We need a new business card design, centered around our new logo (PSD provided below).

Designs that we do like:
https://pixelmarsh.net/item/corporate-business-card/5382017?s_rank=43 (needs to be made more eye catching)

Our main areas of business are:
- Dedicated Servers
- Game Servers
- Voice Servers
- Mitigation Security Specialists

Industry/Entity Type

Business

Contact Information for Business Card

On the card: (and anything else you would suggest)
- Staff member name
- Staff member position in company
- Staff member phone number
- Staff member email
- Other / Staff member Skype
- Website link

Colors
9bcb3c
abd036

Requirements
Must have
• Design of Card:
• - Green (same green as the logo)
• - Business / Corporate design
• - Something a little different / abstract that shouts premium

```html
<!DOCTYPE html>
<html lang="en">
<head>
<meta charset="utf-8">
<title>Brightpath Hosting – Business Card</title>
<link rel="stylesheet" href="https://fonts.googleapis.com/css2?family=Lato:wght@400;700;900&display=swap">
<style>
  :root {
    --green: #9bcb3c;
    --green-light: #abd036;
    --ink: #1d1d1d;
    --panel: #262626;
    --panel-line: #3a3a3a;
    --grey-light: #bdbdbd;
    --stage: #2e2e2e;
  }
  * { box-sizing: border-box; margin: 0; padding: 0; }
  html, body { width: 1200px; height: 873px; overflow: hidden; }
  body {
    background: var(--stage);
    font-family: "Lato", Arial, sans-serif;
    display: flex; flex-direction: column; align-items: center; justify-content: center;
    gap: 40px;
  }
  .card {
    width: 640px; height: 366px; border-radius: 14px; overflow: hidden;
    position: relative; box-shadow: 0 10px 30px rgba(0,0,0,.45);
  }

  /* Brand side */
  .card-brand { background: linear-gradient(135deg, #ffffff, #ececec); }
  .card-brand .brand {
    position: absolute; left: 0; right: 0; top: 0; height: 238px;
    display: flex; align-items: center; justify-content: center; gap: 16px;
  }
  .brand-mark { width: 30px; height: 30px; background: var(--green); border-radius: 4px; flex: none; }
  .brand-name {
    font-weight: 900; font-size: 40px; color: var(--green); letter-spacing: .5px;
    text-transform: uppercase; line-height: 1;
  }
  .services-band {
    position: absolute; left: 0; right: 0; bottom: 0; height: 128px;
    background: linear-gradient(180deg, var(--green-light), var(--green));
    display: flex; flex-direction: column; align-items: center; justify-content: center; gap: 8px;
    color: #fff; font-size: 20px; letter-spacing: .5px;
  }
  .services-band .sep { opacity: .8; margin: 0 10px; }

  /* Contact side */
  .card-contact { background: var(--panel); display: flex; }
  .pattern-panel {
    width: 292px; height: 100%; flex: none; padding: 0 24px;
    background: linear-gradient(140deg, #ffffff 0%, #eeeeee 45%, #dedede 100%);
    display: flex; align-items: center; justify-content: center; flex-direction: column; gap: 16px;
    text-align: center;
  }
  .pattern-panel .brand-name { font-size: 32px; line-height: 1.05; }
  .pattern-panel .brand-mark { width: 48px; height: 48px; border-radius: 6px; }
  .stripes {
    width: 30px; height: 100%; flex: none;
    background: repeating-linear-gradient(90deg, #fff 0 4px, var(--ink) 4px 8px);
  }
  .contact-panel { flex: 1; padding: 26px 28px 0 30px; color: var(--grey-light); }
  .person { text-align: center; padding-bottom: 16px; border-bottom: 1px solid var(--panel-line); }
  .person-name { color: var(--green); font-weight: 700; font-size: 20px; }
  .person-role { font-size: 12px; color: var(--grey-light); margin-top: 4px; }
  .contact-row {
    display: flex; align-items: center; gap: 22px; height: 74px;
    border-bottom: 1px solid var(--panel-line); font-size: 15px; letter-spacing: .3px;
  }
  .contact-row:last-child { border-bottom: none; }
  .icon {
    width: 42px; height: 42px; border-radius: 50%; flex: none;
    border: 2px solid #d9d9d9; background: var(--green);
    display: flex; align-items: center; justify-content: center;
  }
  .icon svg { width: 22px; height: 22px; }
  .contact-lines { display: flex; flex-direction: column; gap: 4px; }
</style>
</head>
<body>

  <section class="card card-brand" aria-label="Business card front">
    <div class="brand">
      <span class="brand-mark"></span>
      <span class="brand-name">Brightpath Hosting</span>
    </div>
    <div class="services-band">
      <p>Dedicated Servers<span class="sep">/</span>Game Servers</p>
      <p>Voice Servers<span class="sep">/</span>Mitigation Security Specialists</p>
    </div>
  </section>

  <section class="card card-contact" aria-label="Business card back">
    <div class="pattern-panel" role="img" aria-label="Soft low-poly geometric background behind the company name">
      <span class="brand-mark"></span>
      <span class="brand-name">Brightpath<br>Hosting</span>
    </div>
    <div class="stripes"></div>
    <div class="contact-panel">
      <div class="person">
        <p class="person-name">Marcus Hale</p>
        <p class="person-role">CEO &amp; Managing Director</p>
      </div>
      <div class="contact-row">
        <span class="icon">
          <svg viewBox="0 0 24 24" fill="#1d1d1d"><path d="M6.6 10.8a15 15 0 0 0 6.6 6.6l2.2-2.2a1 1 0 0 1 1-.25 11.4 11.4 0 0 0 3.6.57 1 1 0 0 1 1 1V20a1 1 0 0 1-1 1A17 17 0 0 1 3 4a1 1 0 0 1 1-1h3.5a1 1 0 0 1 1 1c0 1.25.2 2.45.57 3.6a1 1 0 0 1-.25 1z"/></svg>
        </span>
        <span>02 5550 1947</span>
      </div>
      <div class="contact-row">
        <span class="icon">
          <svg viewBox="0 0 24 24" fill="none" stroke="#1d1d1d" stroke-width="2" stroke-linejoin="round"><path d="M4 5h16v11H10l-4 4v-4H4z"/></svg>
        </span>
        <span>Brightpath.Hosting</span>
      </div>
      <div class="contact-row">
        <span class="icon">
          <svg viewBox="0 0 24 24" fill="none" stroke="#1d1d1d" stroke-width="2"><rect x="3" y="6" width="18" height="12"/><polyline points="3,6 12,13 21,6"/></svg>
        </span>
        <span class="contact-lines">
          <span>info@brightpathhosting.com</span>
          <span>www.brightpathhosting.com</span>
        </span>
      </div>
    </div>
  </section>

</body>
</html>
```